Business card design needed

i need a business card designed for my hair salon its call parlour 71 i want the cards to look similar to the velvet 88 design a big 71 with studio written in the top part of the 3.The 71 big on the left side then all my details (number address name) would love it to be a vintage look, colours to be in black and white/silver card to b black.
to have a line on the back with appointment day time, also would love a vip card like the vip drink card but with free treatments or shampoo so five visits that can b stamped and get a free treatment then 10th get 10% off... or something like that...
Industry/Entity Type
Hair
Contact Information for Business Card
Parlour 71
Mira Dunwoody
0431279406
71 Orchard Crescent, Tallow Bend

```html
<!DOCTYPE html>
<html lang="en">
<head>
<meta charset="utf-8">
<title>Parlour 71 — Loyalty &amp; Business Cards</title>
<link rel="stylesheet" href="https://fonts.googleapis.com/css2?family=Kaushan+Script&family=Questrial&display=swap">
<style>
  :root {
    --ink: #000000;
    --paper: #ffffff;
    --canvas: #ffffff;
    --edge: #1a1a1a;
  }
  * { box-sizing: border-box; margin: 0; padding: 0; }
  html, body {
    width: 1200px;
    height: 459px;
    overflow: hidden;
    background: var(--canvas);
  }
  .canvas {
    position: relative;
    width: 1200px;
    height: 459px;
  }
  .card {
    position: absolute;
    top: 88px;
    width: 480px;
    height: 276px;
    background: var(--paper);
    border: 1.5px solid var(--edge);
    color: var(--ink);
    overflow: hidden;
  }
  .card--loyalty { left: 62px; }
  .card--contact { left: 658px; }

  /* Brand name set as text */
  .brand {
    position: absolute;
    display: flex;
    align-items: center;
    font-family: "Kaushan Script", cursive;
    font-weight: 400;
    color: var(--ink);
    white-space: nowrap;
  }
  .brand__dot {
    display: block;
    border-radius: 50%;
    background: var(--ink);
    flex: none;
  }
  .card--loyalty .brand { left: 22px; top: 62px; font-size: 20px; gap: 7px; }
  .card--loyalty .brand__dot { width: 14px; height: 14px; }
  .card--contact .brand { left: 26px; top: 100px; font-size: 34px; gap: 10px; }
  .card--contact .brand__dot { width: 26px; height: 26px; }

  /* Loyalty card */
  .appointment {
    position: absolute;
    left: 150px;
    top: 30px;
    display: flex;
    align-items: flex-end;
    gap: 6px;
    font-family: "Kaushan Script", cursive;
    font-size: 12px;
    white-space: nowrap;
  }
  .appointment__line {
    display: block;
    width: 185px;
    border-bottom: 1px solid var(--ink);
    margin-bottom: 3px;
  }
  .stamps {
    position: absolute;
    left: 30px;
    top: 126px;
    display: grid;
    grid-template-columns: repeat(5, 44px);
    gap: 26px 22px;
  }
  .stamps__box {
    width: 44px;
    height: 44px;
    border: 5px solid var(--ink);
  }
  .reward {
    position: absolute;
    left: 350px;
    width: 112px;
    font-family: "Questrial", sans-serif;
    font-weight: 700;
    font-size: 12px;
    line-height: 1.25;
    text-align: center;
    letter-spacing: 0.02em;
  }
  .reward--fifth { top: 122px; }
  .reward--tenth { top: 208px; }

  /* Contact card */
  .contact {
    position: absolute;
    right: 30px;
    top: 106px;
    text-align: right;
  }
  .contact__name {
    font-family: "Kaushan Script", cursive;
    font-size: 22px;
    line-height: 1.1;
    white-space: nowrap;
  }
  .contact__phone {
    font-family: "Questrial", sans-serif;
    font-size: 13px;
    letter-spacing: 0.06em;
    margin-top: 4px;
  }
  .address {
    position: absolute;
    left: 160px;
    top: 222px;
    font-family: "Kaushan Script", cursive;
    font-size: 11.5px;
    line-height: 1.35;
    text-align: right;
  }
</style>
</head>
<body>
<main class="canvas">

  <section class="card card--loyalty" aria-label="Loyalty card">
    <div class="brand"><span class="brand__dot"></span>Parlour 71</div>
    <p class="appointment">Appointment day time <span class="appointment__line"></span></p>
    <div class="stamps">
      <span class="stamps__box"></span><span class="stamps__box"></span><span class="stamps__box"></span><span class="stamps__box"></span><span class="stamps__box"></span>
      <span class="stamps__box"></span><span class="stamps__box"></span><span class="stamps__box"></span><span class="stamps__box"></span><span class="stamps__box"></span>
    </div>
    <p class="reward reward--fifth">FREE<br>SHAMPOO /<br>TREATMENT</p>
    <p class="reward reward--tenth">10% OFF</p>
  </section>

  <section class="card card--contact" aria-label="Business card">
    <div class="brand"><span class="brand__dot"></span>Parlour 71</div>
    <div class="contact">
      <p class="contact__name">Mira Dunwoody</p>
      <p class="contact__phone">0431279406</p>
    </div>
    <p class="address">71 Orchard Crescent,<br>Tallow Bend</p>
  </section>

</main>
</body>
</html>
```